Wedding "Survival Kit" Bag label

I saw a "Wedding Week Survival Kit" that someone create via this site. They had the same design printed twice (facing opposite directions) on the front of the oversized card and then folded it to top off a bag filled with goodies for their guests. That is what I'm looking to go as well as need help with the design for the card. We are getting married in the Riviera Maya on August 2nd, 2015 and both love very modern designs. Our names are Meris Dolvane and Otto Flemmerik.

We would like the label to say something like "Wedding Survival Kit" and have some type of cool, abs tract logo that includes our first names, the location and maybe even the date. Feel free to visit our wedding website for inspiration: www.merisandotto.example

Industry/Entity Type

Wedding

Font styles to use
Other font styles liked:
• Chalkduster or anything fun

Requirements
Must have
• A fun flare to it!! Bright colors are encouraged!
Should not have
• Traditional boring fonts, or basic design

```html
<!DOCTYPE html>
<html lang="en">
<head>
<meta charset="utf-8">
<title>Wedding Survival Kit — Meris &amp; Otto</title>
<link rel="stylesheet" href="https://fonts.googleapis.com/css2?family=Itim&family=Raleway:wght@300&family=Share+Tech+Mono&display=swap">
<style>
  :root {
    --teal: #0b7f7d;
    --white: #ffffff;
    --coral: #f25a5a;
    --ink: #1a1a1a;
  }
  html, body {
    margin: 0;
    padding: 0;
    overflow: hidden;
    background: var(--teal);
  }
  .label {
    position: relative;
    width: 1200px;
    height: 773px;
    background: var(--teal);
    overflow: hidden;
  }
  .stripes {
    position: absolute;
    inset: 0;
  }
  .panel {
    position: absolute;
    left: 133px;
    top: 69px;
    width: 936px;
    height: 627px;
    background: var(--white);
  }
  .title {
    position: absolute;
    left: 0;
    right: 0;
    top: 72px;
    margin: 0;
    text-align: center;
    font-family: "Itim", cursive;
    font-weight: 400;
    font-size: 86px;
    line-height: 94px;
    color: var(--coral);
    letter-spacing: 2px;
  }
  .rule {
    position: absolute;
    height: 5px;
    background: var(--coral);
  }
  .rule-left { left: 133px; width: 348px; }
  .rule-right { left: 725px; width: 344px; }
  .rule-upper { top: 385px; }
  .rule-lower { top: 408px; }
  .ampersand {
    position: absolute;
    left: 500px;
    width: 200px;
    top: 285px;
    text-align: center;
    font-family: "Raleway", sans-serif;
    font-weight: 300;
    font-size: 215px;
    line-height: 240px;
    color: var(--coral);
  }
  .name {
    position: absolute;
    top: 397px;
    width: 200px;
    margin-top: -22px;
    text-align: center;
    font-family: "Share Tech Mono", monospace;
    font-size: 42px;
    line-height: 44px;
    letter-spacing: 4px;
    color: var(--ink);
  }
  .name-bride { left: 420px; transform: rotate(-90deg); }
  .name-groom { left: 585px; transform: rotate(90deg); }
  .details {
    position: absolute;
    left: 0;
    right: 0;
    top: 553px;
    margin: 0;
    text-align: center;
    font-family: "Share Tech Mono", monospace;
    font-size: 47px;
    line-height: 60px;
    letter-spacing: 5px;
    color: var(--ink);
  }
</style>
</head>
<body>
<main class="label">
  <svg class="stripes" width="1200" height="773" viewBox="0 0 1200 773" aria-hidden="true">
    <g fill="#ffffff">
      <rect x="22" y="0" width="3" height="773"/>
      <rect x="37" y="0" width="3" height="773"/>
      <rect x="122" y="0" width="3" height="773"/>
      <rect x="140" y="0" width="3" height="773"/>
      <rect x="160" y="0" width="3" height="773"/>
      <rect x="178" y="0" width="3" height="773"/>
      <rect x="588" y="0" width="3" height="773"/>
      <rect x="645" y="0" width="3" height="773"/>
      <rect x="658" y="0" width="3" height="773"/>
      <rect x="1032" y="0" width="3" height="773"/>
      <rect x="1080" y="0" width="3" height="773"/>
      <rect x="1155" y="0" width="3" height="773"/>
      <rect x="1175" y="0" width="3" height="773"/>
    </g>
  </svg>

  <section class="panel"></section>

  <h1 class="title">WEDDING<br>SURVIVAL KIT</h1>

  <div class="rule rule-left rule-upper"></div>
  <div class="rule rule-left rule-lower"></div>
  <div class="rule rule-right rule-upper"></div>
  <div class="rule rule-right rule-lower"></div>

  <div class="name name-bride">MERIS</div>
  <div class="ampersand">&amp;</div>
  <div class="name name-groom">OTTO</div>

  <p class="details">RIVIERA MAYA<br>AUGUST 2nd, 2015</p>
</main>
</body>
</html>
```